Homepage design for Dutch Job Posting Site (Varo-Plek.nl)

We need a redesign of our homepage www.Varo-Plek.nl to make it very clear what we do. We are an online job posting portal and are looking to recruit clients and professionals on a single page.

The Homepage will focus on CLIENTS (OPDRACHTGEVERS), with the idea that if we have a lot of jobs posted, then the professionals will come.

Important to know is that we now have ONE REGISTRATION for both professionals and clients - so there is no need for two separate registration options.

Also important to know is that the JOB POSTER pages will have a GREEN hyperlinks color (see the color above the OPDRACHTGEVER at the top of the screen) and the Professionals will have a BLUE hyperlinks color (see the color above the PROFESSIONAL at the top of the screen).

At the top of the page, we would like a 4 page slider (we will do the coding but just want 4 slides) that shows how it works and what makes us unique. In the examples below, you can see that we have already done 2 of them, and we will ask the designer to help do the other two once the project is awarded.

You can see from the images provided that we have already done most of the work. The HEADER WRAP and the FOOTER are already done, and you can use these in your examples.

Notice also in the image "Homepage-BannerBlank" the image used in the center. It is an image that is only as wide as the header and then fades off into a background image that we can use repeat-x in the css of the site which fills the screen on any monitor resolution. If you don't understand what I just wrote, you probably are not the right designer for the job.

Notice also that the two images "NU AANMELDEN" and "VARO-PLEK ESCROW" use background images that have a SUBTLE background image - it is not just a gradient color change. This is what we LOVE in the design so far.

You can see that our design is already very far advanced, so what we are looking for in a new design are not the overall redesign, but specific, subtle design improvements to give the page a CLEAN, FRESH, MODERN look without being busy and crowded.

Where we specifically want help is in these areas. The designers that show us these elements will be the ones selected. All others will be eliminated without further comment:
a) How to blend in the Varo-Plek logo into the header design without taking up more HEIGHT (we have done a white overlay, but this is where you can prove to us that you are great.

b) We need a font for our h1 tags in our site. This will be the same font used in "Laatste Opdrachten" "Laatste Blogs" "Zoek uw professional per categorie of rubriek". Do not use a webfont (Arial or Verdana). Instead, refer to the examples provided for inspiration of a font that best suits the site for a header.

c) We need better containers for "Laatse opdrachten", "Laatste Blogs" and Zoek uw professional per categorie of rubriek. They can have colors or just borders or just outlines. They should compliment the site look though and not distract from it.

d) Transitions between the containers and other elements. Right now they are all just boxy and separate, but there could be some overlap, some shadows, an image divider (as there is between "Laatste Blogs" and TarnoRadio) but again, the transitions need top complement the design and not take it over.

Sites that appeal to us for what we are looking for are:
- brisket.com
- www.lumivault.com*
- Tallyforge.com*
- Quendalux.com*
*What we like here are both the top PROMINENT central message and then the smaller subtler design transitions underneath.

Feel free to use images or icons to complement the look, but it must be clean, fresh and modern.

Target Market(s)

University-educated Job Posters between 18 - 45

Industry/Entity Type

Online

Requirements
Must have
• - The header wrapper height but be exactly as it is on the images given. This header will be used on all the inner pages and therefore cannot be any higher than what is shown.
- Focus on the 4 tasks outlined
- Keep it clean! We love white, but also like small icons where appropriate and clean transitions.
Nice to have
• Dutch text is NOT important, we can translate.
Should not have
• No cluttered design.

```html
<!DOCTYPE html>
<html lang="nl">
<head>
<meta charset="utf-8">
<title>Varo-Plek – Opdrachten en professionals</title>
<link rel="stylesheet" href="https://fonts.googleapis.com/css2?family=Carlito:wght@400;700&family=Questrial&family=Poiret+One&family=Architects+Daughter&display=swap">
<style>
  :root{
    --green:#8cb21c;
    --green-light:#a6d13a;
    --green-pale:#cbe3a0;
    --blue:#2f74ad;
    --blue-btn:#1f8fd8;
    --ink:#1d1d1d;
    --grey-bg:#ececec;
    --grey-line:#cfcfcf;
    --black:#141414;
    --white:#ffffff;
  }
  *{box-sizing:border-box;margin:0;padding:0}
  html,body{width:833px;height:1200px;overflow:hidden}
  body{position:relative;background:var(--grey-bg);font-family:"Carlito",sans-serif;color:var(--ink)}
  .abs{position:absolute}

  /* header */
  .site-header{left:0;top:0;width:833px;height:115px;background:var(--grey-bg)}
  .brand{left:28px;top:30px;display:flex;align-items:center;gap:10px}
  .brand-mark{width:52px;height:52px;border-radius:50%;background:var(--green)}
  .brand-name{font-family:"Questrial",sans-serif;font-size:46px;line-height:46px;color:#3a3a3a}
  .search-top{left:428px;top:0;width:394px;height:50px;background:#222;border-radius:0 0 12px 12px}
  .search-top .label{position:absolute;left:36px;top:17px;color:var(--white);font-size:16px}
  .search-top .select{position:absolute;left:95px;top:13px;width:239px;height:27px;border-radius:14px;background:linear-gradient(#f4f4f4,#d6d6d6);font-size:11px;padding:6px 16px;color:#333}
  .search-top .select::after{content:"";position:absolute;right:10px;top:10px;border:5px solid transparent;border-top:7px solid #888}
  .search-top .go{position:absolute;left:343px;top:10px;width:35px;height:35px;border-radius:50%;background:radial-gradient(circle at 40% 35%,#b6e04a,#5f9410)}

  /* nav */
  .main-nav{left:0;top:115px;width:833px;height:37px;background:linear-gradient(#2a2a2a,#050505)}
  .main-nav a{position:absolute;top:9px;color:var(--white);font-size:15px;text-decoration:none}
  .main-nav a.active{top:6px;padding:3px 14px;background:linear-gradient(var(--green-light),#6e9b14);border-radius:4px;border:1px solid #c6ea7a}

  /* hero */
  .hero{left:0;top:152px;width:833px;height:336px;background:var(--white);overflow:hidden}
  .hero .circle{position:absolute;border-radius:50%}
  .hero .c1{left:25px;top:25px;width:210px;height:210px;background:#efefef}
  .hero .c2{left:200px;top:33px;width:162px;height:162px;background:#eef6d9}
  .hero .skyline{position:absolute;left:0;bottom:0;width:833px;height:80px;background:var(--green-pale)}
  .hero .photo{position:absolute;left:462px;top:14px;width:328px;height:306px;background:linear-gradient(#e2e2e2,#9a9a9a);border-radius:6px}
  .hero h1{position:absolute;left:98px;top:94px;font-family:"Carlito",sans-serif;font-weight:400;font-size:57px;color:var(--green)}
  .hero h2{position:absolute;left:142px;top:160px;font-weight:400;font-size:24px;color:#333}
  .hero .dots{position:absolute;left:182px;top:207px;display:flex;gap:8px}
  .hero .dots span{width:18px;height:18px;border-radius:50%;background:#e4e4e4;border:1px solid #bbb}
  .hero .dots span.on{background:var(--green);border-color:#6e9b14}

  /* search panels */
  .finder{left:33px;top:503px;width:772px;height:180px;border:1px solid var(--grey-line);border-radius:0 0 12px 12px;background:linear-gradient(#fafafa,#cfcfcf);display:flex}
  .finder-col{position:relative;width:50%;height:100%}
  .finder-col+.finder-col{border-left:1px solid var(--grey-line)}
  .pill{position:absolute;left:32px;top:-2px;width:314px;height:26px;border-radius:13px;background:linear-gradient(var(--green-light),#6e9b14);text-align:center;font-family:"Questrial",sans-serif;font-size:18px;line-height:26px;color:#111}
  .pill em{font-style:normal;color:var(--white)}
  .field{position:absolute;left:38px;top:48px;width:289px;height:29px;background:var(--white);border-radius:4px;font-size:11px;padding:8px 11px;box-shadow:inset 0 1px 2px #ccc}
  .dropdown{position:absolute;left:38px;top:91px;width:165px;height:28px;background:linear-gradient(#fff,#e2e2e2);border-radius:4px;font-size:11px;padding:7px 9px}
  .dropdown::after{content:"";position:absolute;right:10px;top:11px;border:5px solid transparent;border-top:7px solid #888}
  .btn-grey{position:absolute;left:211px;top:91px;width:113px;height:28px;border-radius:4px;background:linear-gradient(#bdbdbd,#7e7e7e);color:var(--white);font-size:16px;text-align:center;line-height:28px}
  .hint{position:absolute;left:41px;top:133px;font-size:10px}

  /* call to action */
  .cta{left:36px;top:690px;width:769px;height:86px;background:#e4e4e4;border:1px solid #d0d0d0}
  .cta p{position:absolute;left:10px;top:18px;font-family:"Poiret One",sans-serif;font-weight:700;font-size:29px;color:var(--blue);letter-spacing:-1px}
  .btn-blue{position:absolute;left:566px;top:20px;width:197px;height:35px;border-radius:5px;background:linear-gradient(#4ab3f2,var(--blue-btn));color:var(--white);font-family:"Poiret One",sans-serif;font-weight:700;font-size:23px;text-align:center;line-height:34px}
  .cta .klik{position:absolute;left:484px;top:58px;font-family:"Architects Daughter",cursive;font-size:17px}
  .cta svg{position:absolute;left:554px;top:50px}

  /* listings */
  .section-title{left:40px;top:790px;font-family:"Questrial",sans-serif;font-weight:400;font-size:20px}
  .section-title em{font-style:normal;color:var(--green)}
  .see-all{left:706px;top:794px;font-size:14px;color:var(--green)}
  .job{left:44px;width:753px;height:110px;background:linear-gradient(#fff,#f1f1f1);border:1px solid #e0e0e0;border-radius:5px}
  .job h3{position:absolute;left:11px;top:12px;font-weight:400;font-size:14px}
  .job .cat{position:absolute;left:11px;top:33px;font-size:10.5px}
  .job .desc{position:absolute;left:11px;top:45px;width:735px;font-size:10.5px;line-height:12.5px}
  .job .age{position:absolute;right:18px;top:4px;font-size:10.5px}
  .job .more{position:absolute;right:20px;top:80px;font-size:15px;color:var(--blue)}
  .job svg{position:absolute;left:604px;top:108px}
  .job .ago{position:absolute;left:641px;top:119px;font-size:10.5px}

  /* footer */
  .site-footer{left:0;top:1113px;width:833px;height:87px;background:var(--black)}
  .site-footer a{position:absolute;top:16px;color:var(--white);font-size:15px;text-decoration:none}
  .site-footer small{position:absolute;left:24px;top:61px;color:#ddd;font-size:9px}
  .social{position:absolute;left:666px;top:50px;display:flex;gap:7px}
  .social span{width:22px;height:22px;border-radius:50%;background:#f2f2f2}
</style>
</head>
<body>

<header class="site-header abs">
  <div class="brand abs">
    <div class="brand-mark"></div>
    <div class="brand-name">Varo-Plek</div>
  </div>
  <div class="search-top abs">
    <span class="label">Zoeken</span>
    <div class="select">Zoek opdrachten</div>
    <div class="go"></div>
  </div>
</header>

<nav class="main-nav abs">
  <a class="active" style="left:89px">Home</a>
  <a style="left:189px">Opdrachten</a>
  <a style="left:315px">Mijn Kantoor</a>
  <a style="left:453px">Hoe het werkt</a>
  <a style="left:601px">Blog</a>
  <a style="left:687px">Contact</a>
</nav>

<section class="hero abs">
  <div class="circle c1"></div>
  <div class="circle c2"></div>
  <div class="skyline" role="img" aria-label="Light green city skyline silhouette"></div>
  <div class="photo" role="img" aria-label="Group of cheerful professionals in business suits jumping in the air"></div>
  <h1>What makes</h1>
  <h2>Professionals happy</h2>
  <div class="dots"><span></span><span class="on"></span><span></span><span></span></div>
</section>

<section class="finder abs">
  <div class="finder-col">
    <div class="pill">Zoek <em>Professionals</em></div>
    <div class="field">Vul hier uw zoekopdracht in</div>
    <div class="dropdown">Alle Categorieen</div>
    <div class="btn-grey">Zoeken</div>
    <p class="hint">De juiste Professional vinden voor uw opdracht</p>
  </div>
  <div class="finder-col">
    <div class="pill">Zoek <em>Opdrachten</em></div>
    <div class="field">Vul hier uw zoekopdracht in</div>
    <div class="dropdown">Alle Categorieen</div>
    <div class="btn-grey">Zoeken</div>
    <p class="hint" style="top:130px">Verdien geld door de juiste Opdracht te vinden</p>
  </div>
</section>

<section class="cta abs">
  <p>Wilt u dat professionals vechten om uw opdracht?</p>
  <div class="btn-blue">Opdracht Plassen</div>
  <span class="klik">Klik hire</span>
  <svg width="36" height="30" viewBox="0 0 36 30"><path d="M2 26 Q22 26 30 6" fill="none" stroke="#222" stroke-width="1.5"/><path d="M24 9 L30 4 L31 12" fill="none" stroke="#222" stroke-width="1.5"/></svg>
</section>

<h2 class="section-title abs">Laatste <em>Opdrachten</em></h2>
<span class="see-all abs">Alles Bekijken</span>

<article class="job abs" style="top:827px">
  <span class="age">1 maand geleden</span>
  <h3>VOIP telefonie in kantoor instellen</h3>
  <span class="cat">IT</span>
  <p class="desc">Voor mijn kantoor tot 5 werkplekken ben ik op zoek naar een bedrijf dat de telefonie voor mij op de juiste wijze kan instellen. Ik heb een Veltro online nummer, wat het vaste telefoonnummer moet worden, waarop alle medewerkers te bereiken zijn. Verder moet er doorverbonden kunnen worden naar specifi....</p>
  <span class="more">Opdracht bekijken</span>
  <svg width="20" height="18" viewBox="0 0 20 18"><path d="M0 0 L20 0 L16 18 Z" fill="#f1f1f1" stroke="#e0e0e0"/></svg>
  <span class="ago">12 days ago</span>
</article>

<article class="job abs" style="top:969px">
  <span class="age">1 maand geleden</span>
  <h3>VOIP telefonie in kantoor instellen</h3>
  <span class="cat">IT</span>
  <p class="desc">Voor mijn kantoor tot 5 werkplekken ben ik op zoek naar een bedrijf dat de telefonie voor mij op de juiste wijze kan instellen. Ik heb een Veltro online nummer, wat het vaste telefoonnummer moet worden, waarop alle medewerkers te bereiken zijn. Verder moet er doorverbonden kunnen worden naar specifi....</p>
  <span class="more">Opdracht bekijken</span>
  <svg width="20" height="18" viewBox="0 0 20 18"><path d="M0 0 L20 0 L16 18 Z" fill="#f1f1f1" stroke="#e0e0e0"/></svg>
  <span class="ago">12 days ago</span>
</article>

<footer class="site-footer abs">
  <a style="left:26px">Home</a>
  <a style="left:112px">Opdrachten</a>
  <a style="left:238px">Mijn Kantoor</a>
  <a style="left:376px">Hoe het werkt</a>
  <a style="left:524px">Blog</a>
  <a style="left:610px">Contact</a>
  <small>Copyright © 2011.www.varo-plek.com</small>
  <div class="social"><span></span><span></span><span></span><span></span><span></span></div>
</footer>

</body>
</html>
```